依頼詳細
販売商品は下記の3種類です。詳細はURLをご参照下さい。

1.工業用精製水 (用途:実験室などでの試験器具洗浄など)
http://www.hanabo-tenko.com/shop/goods/goods/goods.php?act=Goods&mode=Detail&id=00054986

2.バッテリー補充液 (用途:バッテリーの補充液など)
http://www.hanabo-tenko.com/shop/goods/goods/goods.php?act=Goods&mode=Detail&id=00054987

3.高純度精製水 (用途:エステスチーマーや加湿器の補給水など)
http://www.hanabo-tenko.com/shop/goods/goods/goods.php?act=Goods&mode=Detail&id=00066908

精製水は純度の高い水(きれいな水)ですので、商品に相応しい爽やかな印象を持っていただけるデザインを希望します。全体的にブルー系統のカラーを希望します。

添付の原案のレイアウト通りの必要はありません。見やすく目的に沿った内容であれば、画像等の追加、文章やフレーズ、フォント、文字サイズなどの修正、加筆もOKです。基本的にはデザインを重視したいと思います。

記載事項が多いので、A4サイズに収まるレイアウトの工夫をお願い致します。
記載項目
添付の【原案】をご参照下さい。
サイズ
A4
ページ数
両面
希望イメージ
シンプル 複雑
単色 カラフル
暗い 明るい
日常 高級
遊び心 厳粛
未来的 伝統的
女性的 男性的
希望する色
水色系
納品ファイル
• 高解像度JPG (.jpg)
• イラストレーター形式 (.ai)
補足説明

当社の要望・イメージに最も近いデザインでした。

みなさん非常に素晴らしいご提案でしたので、選定に苦慮いたしました。

選定できなかった皆様には申し訳ございませんでしたが、またの機会がございましたらよろしくお願い致します。皆様のご尽力にとても感謝致します。

この度は誠にありがとうございました。

```html
<!DOCTYPE html>
<html lang="ja">
<head>
<meta charset="utf-8">
<title>注文シート(FAX専用)</title>
<link rel="stylesheet" href="https://fonts.googleapis.com/css2?family=Noto+Sans+JP:wght@400;500;700;900&display=swap">
<style>
:root{
  --ink:#163a5c;
  --text:#1d2b38;
  --bar:#1f72b8;
  --accent:#45a6de;
  --line:#9cc7e6;
  --soft:#cfe4f3;
  --pale:#eaf5fc;
  --wash:#f4fafe;
  --paper:#ffffff;
}
*{box-sizing:border-box;margin:0;padding:0}
html,body{width:849px;height:1200px;overflow:hidden;background:var(--paper)}
body{font-family:"Noto Sans JP",sans-serif;color:var(--text);font-size:9px;line-height:1.3}
.sheet{position:relative;width:849px;height:1200px;padding:18px 24px}
.top{display:flex;align-items:center;height:92px;gap:14px}
.fax-dir{width:78px;height:74px;border:2px solid var(--ink);display:flex;flex-direction:column;align-items:center;justify-content:flex-end;padding-bottom:4px;font-size:8px;font-weight:700;color:var(--ink)}
.fax-dir svg{margin-bottom:4px}
.copy-note{width:92px;font-size:9px;line-height:1.5;text-align:center}
.title{flex:1;text-align:center;font-size:34px;font-weight:900;letter-spacing:1px;color:var(--ink)}
.order-date{width:180px;border:1.5px solid var(--bar)}
.order-date .h{background:var(--bar);color:#fff;text-align:center;font-weight:700;padding:2px}
.order-date .b{height:28px;display:flex;align-items:center;justify-content:space-around;font-size:10px}
.row{display:flex;gap:14px;margin-top:12px}
.col{flex:1}
.sec-h{background:var(--bar);color:#fff;font-weight:700;font-size:10px;padding:3px 8px;display:flex;justify-content:space-between;align-items:center}
.sec-h small{font-weight:400;font-size:8px;color:#dcedf9}
.sec-b{border:1.5px solid var(--bar);border-top:none}
.field{display:flex;border-bottom:1px solid var(--soft);min-height:24px}
.field:last-child{border-bottom:none}
.field .lb{width:70px;background:var(--pale);font-size:8px;padding:3px 5px;display:flex;align-items:center;color:var(--ink)}
.field .val{flex:1}
.field.tall{min-height:42px}
.field.tall .lb{align-items:flex-start}
.check{display:inline-block;width:11px;height:11px;border:1.3px solid var(--ink);vertical-align:middle;margin-right:4px;background:#fff}
.pay{display:flex;padding:8px;gap:10px;height:160px}
.pay-list{width:100px;display:flex;flex-direction:column;gap:36px;font-weight:700;font-size:11px;padding-top:8px;color:var(--ink)}
.pay-note{flex:1;font-size:8px;line-height:1.6}
.doc-box{border:1.3px solid var(--accent);background:var(--wash);padding:5px 8px;margin-bottom:6px;font-size:9px;line-height:1.8}
.slip{padding:8px;height:160px;font-size:10px}
.slip p{margin-bottom:8px;font-weight:700;color:var(--ink)}
.slip p span{font-weight:400;font-size:8px;color:var(--text)}
table{border-collapse:collapse;width:100%}
td,th{border:1px solid var(--line);padding:2px 4px;font-size:8.5px;text-align:center}
th{background:var(--pale);font-weight:700;color:var(--ink)}
.fee{width:180px;margin-top:4px}
.products{display:flex;gap:8px;padding:6px}
.product{flex:1}
.product .ph{background:var(--accent);color:#fff;font-weight:700;font-size:10px;display:flex;justify-content:space-between;padding:3px 6px}
.product td{height:20px}
.product td.qty{width:32%;background:var(--wash)}
.product td.box{width:30%;text-align:right}
.total{display:flex;justify-content:flex-end;align-items:center;padding:4px 6px 6px;gap:8px;font-size:9px}
.total .line{width:220px;border-bottom:1.5px solid var(--ink);height:20px;text-align:right;font-weight:700}
.notes{font-size:8px;padding:3px 6px}
.date-box{display:flex;justify-content:space-around;align-items:center;height:42px;font-size:11px;font-weight:700;color:var(--ink)}
.times{display:grid;grid-template-columns:1fr 1fr;gap:6px 10px;padding:8px 14px;font-size:10px;font-weight:700;color:var(--ink)}
.opinion{height:122px;padding:6px;font-size:8px}
.fax-band{position:absolute;left:24px;right:24px;bottom:18px;height:130px;border-top:3px solid var(--bar);background:linear-gradient(180deg,var(--pale),var(--paper));display:flex;flex-direction:column;align-items:center;justify-content:center}
.fax-band .num{font-size:48px;font-weight:900;letter-spacing:1px;color:var(--ink)}
.fax-band .sub{font-size:12px;font-weight:500;color:var(--bar)}
</style>
</head>
<body>
<div class="sheet">
  <header class="top">
    <div class="fax-dir">
      <svg width="40" height="36" viewBox="0 0 40 36"><polygon points="20,0 40,20 28,20 28,36 12,36 12,20 0,20" fill="#1f72b8"/></svg>
      FAX送信方向
    </div>
    <div class="copy-note">本紙はあらかじめ<br>コピーして<br>ご使用下さい。</div>
    <h1 class="title">注文シート(FAX専用)</h1>
    <div class="order-date"><div class="h">ご注文日</div><div class="b"><span>平成</span><span>年</span><span>月</span><span>日</span></div></div>
  </header>

  <div class="row">
    <section class="col">
      <div class="sec-h">【ご注文者様情報】<small>※必須項目をご記入下さい</small></div>
      <div class="sec-b">
        <div class="field"><div class="lb">フリガナ</div><div class="val"></div></div>
        <div class="field tall"><div class="lb">氏名・会社名</div><div class="val"></div></div>
        <div class="field tall"><div class="lb">住所 〒</div><div class="val"></div></div>
        <div class="field"><div class="lb">電話番号</div><div class="val"></div></div>
        <div class="field"><div class="lb">FAX番号</div><div class="val"></div></div>
        <div class="field"><div class="lb">E-mail</div><div class="val"></div></div>
      </div>
    </section>
    <section class="col">
      <div class="sec-h">【お届け先情報】<small>※ご注文者様と異なる場合のみ</small></div>
      <div class="sec-b">
        <div class="field"><div class="lb">フリガナ</div><div class="val"></div></div>
        <div class="field tall"><div class="lb">氏名・会社名</div><div class="val"></div></div>
        <div class="field tall"><div class="lb">住所 〒</div><div class="val"></div></div>
        <div class="field"><div class="lb">電話番号</div><div class="val"></div></div>
        <div class="field"><div class="lb">FAX番号</div><div class="val"></div></div>
        <div class="field"><div class="lb">E-mail</div><div class="val"></div></div>
      </div>
    </section>
  </div>

  <div class="row">
    <section class="col">
      <div class="sec-h">【お支払い方法】<small>※ご希望のお支払い方法に☑して下さい</small></div>
      <div class="sec-b pay">
        <div class="pay-list"><div><span class="check"></span>銀行振込</div><div><span class="check"></span>代金引換</div></div>
        <div class="pay-note">
          <div class="doc-box">ご請求書・領収書<br><span class="check"></span>ご注文者様宛に送付<br><span class="check"></span>お届け先様宛に送付</div>
          ※振込手数料はお客様のご負担となります。<br>ご入金確認後の発送となります。<br>代金引換の場合は別途手数料がかかります。
        </div>
      </div>
    </section>
    <section class="col">
      <div class="sec-h">【伝票発行】<small>※ご希望の項目に☑して下さい</small></div>
      <div class="sec-b slip">
        <p><span class="check"></span>納品書 <span>商品発送時に同梱いたします</span></p>
        <p><span class="check"></span>領収書 <span>宛名：</span></p>
        <table class="fee">
          <tr><th>代引金額</th><th>代引手数料</th></tr>
          <tr><td>1万円未満</td><td>315円</td></tr>
          <tr><td>3万円未満</td><td>420円</td></tr>
          <tr><td>10万円未満</td><td>630円</td></tr>
          <tr><td>30万円未満</td><td>1,050円</td></tr>
        </table>
      </div>
    </section>
  </div>

  <section class="row" style="display:block">
    <div class="sec-h">【ご注文内容】<small>※ご注文数をご記入下さい</small></div>
    <div class="sec-b">
      <div class="products">
        <div class="product">
          <div class="ph"><span>工業用精製水</span><span>ISP-01</span></div>
          <table>
            <tr><td class="qty">1ケース</td><td>4,725円</td><td class="box">箱</td></tr>
            <tr><td class="qty">2ケース</td><td>9,030円</td><td class="box">箱</td></tr>
            <tr><td class="qty">3ケース</td><td>13,230円</td><td class="box">箱</td></tr>
            <tr><td class="qty">4ケース</td><td>17,220円</td><td class="box">箱</td></tr>
            <tr><td class="qty">5ケース</td><td>21,000円</td><td class="box">箱</td></tr>
            <tr><td class="qty">10ケース</td><td>40,950円</td><td class="box">箱</td></tr>
          </table>
        </div>
        <div class="product">
          <div class="ph"><span>バッテリー補充液</span><span>TSP-02</span></div>
          <table>
            <tr><td class="qty">1ケース</td><td>4,725円</td><td class="box">箱</td></tr>
            <tr><td class="qty">2ケース</td><td>9,030円</td><td class="box">箱</td></tr>
            <tr><td class="qty">3ケース</td><td>13,230円</td><td class="box">箱</td></tr>
            <tr><td class="qty">4ケース</td><td>17,220円</td><td class="box">箱</td></tr>
            <tr><td class="qty">5ケース</td><td>21,000円</td><td class="box">箱</td></tr>
            <tr><td class="qty">10ケース</td><td>40,950円</td><td class="box">箱</td></tr>
          </table>
        </div>
        <div class="product">
          <div class="ph"><span>高純度精製水</span><span>TSP-03</span></div>
          <table>
            <tr><td class="qty">1ケース</td><td>5,250円</td><td class="box">箱</td></tr>
            <tr><td class="qty">2ケース</td><td>10,080円</td><td class="box">箱</td></tr>
            <tr><td class="qty">3ケース</td><td>14,805円</td><td class="box">箱</td></tr>
            <tr><td class="qty">4ケース</td><td>19,320円</td><td class="box">箱</td></tr>
            <tr><td class="qty">5ケース</td><td>23,625円</td><td class="box">箱</td></tr>
            <tr><td class="qty">10ケース</td><td>46,200円</td><td class="box">箱</td></tr>
          </table>
        </div>
      </div>
      <div class="total"><span>※1ケース=4本入り。価格は税込です。</span><span>合計金額</span><div class="line">円</div></div>
    </div>
  </section>

  <div class="row">
    <section class="col">
      <div class="sec-h">【送料】<small>※地域により異なります</small></div>
      <div class="sec-b">
        <table>
          <tr><th>お届け地域</th><th>1～2ケース</th><th>3ケース以上</th></tr>
          <tr><td>関東・中部</td><td>525円</td><td>無料</td></tr>
          <tr><td>関西・東北</td><td>630円</td><td>無料</td></tr>
          <tr><td>中国・四国</td><td>735円</td><td>無料</td></tr>
          <tr><td>九州</td><td>840円</td><td>無料</td></tr>
          <tr><td>北海道・沖縄</td><td>1,260円</td><td>525円</td></tr>
        </table>
      </div>
    </section>
    <section class="col">
      <div class="sec-h">【お届け希望日】<small>※ご希望がある場合のみ</small></div>
      <div class="sec-b">
        <div class="date-box"><span>平成</span><span>年</span><span>月</span><span>日</span></div>
      </div>
      <div class="sec-h" style="margin-top:6px">【お届け希望時間】<small>※ご希望の時間に☑して下さい</small></div>
      <div class="sec-b times">
        <span><span class="check"></span>午前中</span><span><span class="check"></span>16時～18時</span>
        <span><span class="check"></span>12時～14時</span><span><span class="check"></span>18時～20時</span>
        <span><span class="check"></span>14時～16時</span><span><span class="check"></span>19時～21時</span>
      </div>
    </section>
  </div>

  <div class="row">
    <section class="col">
      <div class="sec-h">【当社への商品のご連絡】</div>
      <div class="sec-b">
        <table>
          <tr><th>商品名</th><th>ご連絡内容</th><th>対応</th></tr>
          <tr><td>&nbsp;</td><td></td><td></td></tr>
          <tr><td>&nbsp;</td><td></td><td></td></tr>
          <tr><td>&nbsp;</td><td></td><td></td></tr>
        </table>
        <div class="notes">※商品到着後7日以内にご連絡下さい。</div>
      </div>
    </section>
    <section class="col">
      <div class="sec-h">【ご意見・ご要望】</div>
      <div class="sec-b opinion">ご意見・ご要望がございましたらご記入下さい。</div>
    </section>
  </div>

  <footer class="fax-band">
    <div class="num">FAX:0120-555-018</div>
    <div class="sub">FAX番号をお確かめの上送信ください</div>
  </footer>
</div>
</body>
</html>
```